Marlow Air Services E-mail Signature

Need to create an email signature for Marlow Air Services. Signature should include the Marlow logo and the associated TRFC member logo

```html
<!DOCTYPE html>
<html lang="en">
<head>
<meta charset="utf-8">
<title>Marlow Air Services – E-mail Signature</title>
<link rel="stylesheet" href="https://fonts.googleapis.com/css2?family=Poppins:wght@400;600;700&display=swap">
<style>
  :root {
    --navy: #0b3a8d;
    --jet-tone: #7a97d4;
    --white: #ffffff;
    --soft-white: #e6ecf8;
  }
  html, body {
    margin: 0;
    padding: 0;
    width: 1200px;
    height: 320px;
    overflow: hidden;
    background: var(--navy);
  }
  .signature {
    position: relative;
    width: 1200px;
    height: 320px;
    background: var(--navy);
    font-family: "Poppins", sans-serif;
    color: var(--white);
    overflow: hidden;
  }
  .jet-photo {
    position: absolute;
    left: 0;
    top: 0;
    width: 1200px;
    height: 320px;
  }
  .contact {
    position: absolute;
    left: 0;
    width: 1200px;
    margin: 0;
    text-align: center;
    line-height: 1;
  }
  .contact__name {
    top: 77px;
    font-weight: 700;
    font-size: 36px;
    letter-spacing: 0.5px;
  }
  .contact__title {
    top: 124px;
    font-weight: 400;
    font-size: 19px;
    letter-spacing: 6px;
  }
  .contact__line {
    font-weight: 400;
    font-size: 19px;
    color: var(--soft-white);
  }
  .contact__phone { top: 181px; }
  .contact__email { top: 214px; }
  .contact__address { top: 253px; }

  .brand {
    position: absolute;
    left: 940px;
    top: 196px;
    width: 234px;
    display: flex;
    flex-direction: column;
    align-items: center;
  }
  .brand__name {
    margin: 0;
    font-family: "Poppins", sans-serif;
    font-weight: 600;
    font-size: 26px;
    line-height: 1.15;
    text-align: center;
    color: var(--white);
  }
  .partner-badge {
    margin-top: 12px;
    width: 96px;
    height: 22px;
    border-radius: 4px;
    background: var(--white);
    opacity: 0.85;
  }
</style>
</head>
<body>
  <div class="signature">
    <svg class="jet-photo" role="img" aria-label="Faded photograph of a private business jet in flight" viewBox="0 0 1200 320">
      <defs>
        <radialGradient id="jetGlow" cx="0.5" cy="0.5" r="0.5">
          <stop offset="0" stop-color="var(--jet-tone)" stop-opacity="0.5"/>
          <stop offset="0.6" stop-color="var(--jet-tone)" stop-opacity="0.22"/>
          <stop offset="1" stop-color="var(--jet-tone)" stop-opacity="0"/>
        </radialGradient>
      </defs>
      <ellipse cx="560" cy="180" rx="560" ry="150" fill="url(#jetGlow)"/>
    </svg>

    <h1 class="contact contact__name">Graham R. Ellison</h1>
    <p class="contact contact__title">CEO &amp; FOUNDER</p>
    <p class="contact contact__line contact__phone">096-05-4827</p>
    <p class="contact contact__line contact__email">GrahamEllison@marlowair.com</p>
    <p class="contact contact__line contact__address">417 Larkspur Road Westbury, NY 11590</p>

    <div class="brand">
      <p class="brand__name">Marlow<br>Air Services</p>
      <div class="partner-badge" role="img" aria-label="Partner membership badge"></div>
    </div>
  </div>
</body>
</html>
```